TRIVEL Corp Has New Logo Now Needs New Stationary

We just chose our new logo, and now we need a letterhead and envelope design. I would like both to be used via Microsoft Word so I can print both the letterhead and envelopes myself rather than having to the letterhead and envelopes produced by a printing firm. I has attached the new logo and spec sheet provided by the logo designer.

```html
<!DOCTYPE html>
<html lang="en">
<head>
<meta charset="utf-8">
<title>TRIVEL Corp Stationery</title>
<link rel="stylesheet" href="https://fonts.googleapis.com/css2?family=Montserrat:wght@600&family=Roboto:wght@400&display=swap">
<style>
  :root {
    --canvas: #e9e7e3;
    --paper: #ffffff;
    --ink: #3a3a3c;
    --text: #2b2b2b;
    --edge: #3c3c3c;
    --green: #7fbf42;
    --blue: #45ade2;
    --charcoal: #363636;
    --faint: #dbeef7;
  }
  html, body { margin: 0; padding: 0; overflow: hidden; }
  body {
    width: 1200px; height: 727px; position: relative;
    background: var(--canvas);
    font-family: "Roboto", Arial, sans-serif; color: var(--text);
  }
  .sheet, .envelope {
    position: absolute; background: var(--paper);
    border: 1px solid var(--edge); box-sizing: border-box; overflow: hidden;
  }
  .brand-name {
    font-family: "Montserrat", Arial, sans-serif; font-weight: 600;
    color: var(--ink); white-space: nowrap; letter-spacing: 0.5px;
  }
  .brand { position: absolute; display: flex; align-items: center; gap: 8px; }
  .brand-dot { border-radius: 50%; background: var(--green); flex: none; }

  /* Letterhead */
  .letterhead { left: 48px; top: 92px; width: 450px; height: 584px; }
  .letterhead .brand { left: 26px; top: 62px; }
  .letterhead .brand-name { font-size: 22px; }
  .letterhead .brand-dot { width: 14px; height: 14px; }
  .contact {
    position: absolute; left: 310px; top: 24px; padding-left: 8px;
    border-left: 1px solid #9a9a9a; font-size: 9.5px; line-height: 13px;
  }
  .contact-line { display: flex; align-items: center; gap: 4px; }
  .contact-line svg { width: 7px; height: 7px; fill: var(--text); }
  .contact-address { margin-top: 8px; }
  .watermark {
    position: absolute; font-family: "Montserrat", Arial, sans-serif; font-weight: 600;
    color: var(--faint); white-space: nowrap;
  }
  .letterhead .watermark { right: 36px; bottom: 24px; font-size: 22px; }
  .footer-rule { position: absolute; left: 0; right: 0; height: 1px; background: var(--green); }
  .footer-band {
    position: absolute; left: 0; right: 0; background: var(--blue);
    font-size: 8.5px; letter-spacing: 0.8px; color: var(--text);
    display: flex; align-items: center; justify-content: center;
  }
  .letterhead .footer-rule { bottom: 19px; }
  .letterhead .footer-band { bottom: 0; height: 17px; }

  /* Envelope backs */
  .flap {
    position: absolute; left: 0; top: 0; right: 0; height: 82px;
    display: flex; align-items: center; justify-content: center;
  }
  .flap .brand-name { font-size: 20px; }
  .envelope-white { left: 524px; top: 44px; width: 489px; height: 238px; }
  .envelope-white .flap { border-bottom: 1px solid var(--edge); }
  .envelope-charcoal { left: 564px; top: 137px; width: 489px; height: 238px; }
  .envelope-charcoal .flap { background: var(--charcoal); }
  .envelope-blue { left: 616px; top: 230px; width: 490px; height: 238px; }
  .envelope-blue .flap { background: var(--blue); }
  .envelope-green { left: 669px; top: 324px; width: 490px; height: 238px; }
  .envelope-green .flap { background: var(--green); }
  .on-colour { color: #ffffff; }

  /* Envelope front */
  .envelope-front { left: 545px; top: 423px; width: 491px; height: 240px; }
  .envelope-front .brand { left: 22px; top: 62px; }
  .envelope-front .brand-name { font-size: 19px; }
  .envelope-front .brand-dot { width: 12px; height: 12px; }
  .return-address { position: absolute; left: 22px; top: 103px; font-size: 8.5px; }
  .envelope-front .watermark { right: 30px; bottom: 22px; font-size: 14px; }
  .envelope-front .footer-rule { bottom: 19px; }
  .envelope-front .footer-band { bottom: 0; height: 17px; justify-content: flex-start; padding-left: 23px; }
</style>
</head>
<body>
  <section class="sheet letterhead">
    <div class="brand"><span class="brand-dot"></span><span class="brand-name">TRIVEL CORP</span></div>
    <div class="contact">
      <div class="contact-line">
        <svg viewBox="0 0 10 10"><path d="M2 0h2l1 3-1.5 1a6 6 0 0 0 2.5 2.5L7 5l3 1v2c0 1-1 2-2 2A8 8 0 0 1 0 2c0-1 1-2 2-2z"/></svg>
        <span>+123 456 7890</span>
      </div>
      <div class="contact-line">
        <svg viewBox="0 0 10 10"><path d="M0 2h10v6H0zM0 2l5 3.5L10 2" fill="none" stroke="currentColor"/><rect x="0" y="2" width="10" height="6"/></svg>
        <span>info@trivelcorp.com</span>
      </div>
      <div class="contact-address">00, Complex name<br>City name, Zip code 004203</div>
    </div>
    <div class="watermark">TRIVEL</div>
    <div class="footer-rule"></div>
    <div class="footer-band">www.trivelcorp.com</div>
  </section>

  <section class="envelope envelope-white">
    <div class="flap"><span class="brand-name">TRIVEL CORP</span></div>
  </section>
  <section class="envelope envelope-charcoal">
    <div class="flap"><span class="brand-name on-colour">TRIVEL CORP</span></div>
  </section>
  <section class="envelope envelope-blue">
    <div class="flap"><span class="brand-name on-colour">TRIVEL CORP</span></div>
  </section>
  <section class="envelope envelope-green">
    <div class="flap"><span class="brand-name on-colour">TRIVEL CORP</span></div>
  </section>

  <section class="envelope envelope-front">
    <div class="brand"><span class="brand-dot"></span><span class="brand-name">TRIVEL CORP</span></div>
    <div class="return-address">00, Complex name, City name, Zip code 004203</div>
    <div class="watermark">TRIVEL</div>
    <div class="footer-rule"></div>
    <div class="footer-band">www.trivelcorp.com</div>
  </section>
</body>
</html>
```